Clearing a Court Debt Mark - Banner Ad for TR Website

I need a banner ad for a book I'm selling.

The book is about Clearing a Court Debt Mark, that is a County Court Judgment, from a credit report.

I have two websites. I want the banner ad to appear on
www.thornridgelaw.co.uk

It will then link to the new site: https://clearyourrecordguide.co.uk/

The first site already has a lot of traffic from visitors wanting to remove a CCJ. The purpose of that first site was originally for visitors to become clients of the law firm. However, most visitors can't afford legal advice and so I'd like to offer them the book instead.

I would like to see designs that use the colour green. The final design should communicate financial freedom, simplicity and trustworthiness.

Target Market(s)

Individuals who have discovered a CCJ on their credit report

Industry/Entity Type

Law

Font styles to use
Sans Serif

Colors
0054AA
0677BA
7BADD7
CADEEF
E8F1F8
0094D4
00A9DD
6FCCEA
C7EBF8
E9F6FB
00AB8E
00BBA5
67D7C9
C6EFE9
E9F9F6

Requirements
Must have
• Must fit at the end of a blog article, such as this one https://www.thornridgelaw.co.uk/ccj-wrong-address/

```html
<!DOCTYPE html>
<html lang="en">
<head>
<meta charset="utf-8">
<title>Clearing a Court Debt Mark – Banner</title>
<link rel="stylesheet" href="https://fonts.googleapis.com/css2?family=Poppins:wght@400;500;600;700;800&display=swap">
<style>
  :root {
    --page: #ffffff;
    --panel-grey: #ebebeb;
    --panel-white: #ffffff;
    --bar-dark: #262626;
    --ink: #211d26;
    --accent-red: #e8363f;
    --green: #5cb85c;
    --green-light: #7fd36b;
    --green-deep: #3f9c3f;
    --leaf-light: #9fdc8a;
    --leaf-deep: #2f8a3a;
    --text-white: #ffffff;
  }
  * { box-sizing: border-box; margin: 0; padding: 0; }
  html, body {
    width: 1200px; height: 1200px; overflow: hidden;
    background: var(--page);
    font-family: "Poppins", sans-serif;
  }
  .canvas { position: relative; width: 1200px; height: 1200px; }

  .banner {
    position: absolute; left: 78px; top: 381px;
    width: 1045px; height: 435px;
    overflow: hidden;
    box-shadow: 0 2px 10px rgba(0,0,0,0.28);
  }
  .band-top { position: absolute; left: 0; top: 0; width: 100%; height: 244px; background: var(--panel-grey); }
  .band-mid { position: absolute; left: 0; top: 244px; width: 100%; height: 93px; background: var(--panel-white); }
  .band-bottom { position: absolute; left: 0; top: 337px; width: 100%; height: 98px; background: var(--bar-dark); }

  .feature-art { position: absolute; left: 0; top: 0; width: 1045px; height: 435px; }

  .headline-lead {
    position: absolute; left: 46px; top: 36px;
    font-weight: 800; font-size: 50px; line-height: 1;
    color: var(--ink); letter-spacing: 0.5px;
  }
  .headline-main {
    position: absolute; left: 40px; top: 98px;
    font-weight: 800; font-size: 92px; line-height: 1;
    color: var(--accent-red); letter-spacing: 1px;
  }
  .author-pill {
    position: absolute; left: 45px; top: 229px;
    width: 563px; height: 45px; border-radius: 5px;
    background: var(--green);
    display: flex; align-items: center; justify-content: center;
    font-weight: 700; font-size: 29px; letter-spacing: 0.5px;
    color: var(--text-white);
  }
  .author-pill .author-name { color: var(--ink); margin-left: 10px; }
  .tagline {
    position: absolute; left: 46px; top: 283px; width: 560px;
    font-weight: 500; font-size: 12.5px; line-height: 1.35;
    color: var(--ink);
  }
  .availability {
    position: absolute; left: 46px; top: 350px;
    font-weight: 500; font-size: 16px; color: var(--text-white);
    display: flex; align-items: center; gap: 6px; white-space: nowrap;
  }
  .availability .highlight { color: var(--green-light); }
  .availability .store-name { font-weight: 700; font-size: 19px; margin: 0 18px 0 2px; }
  .cta-row { position: absolute; left: 45px; top: 386px; display: flex; }
  .cta-button {
    width: 152px; height: 30px; border-radius: 5px 0 0 5px;
    background: linear-gradient(to bottom, var(--green-light), var(--green-deep));
    color: var(--ink); font-weight: 600; font-size: 18px;
    display: flex; align-items: center; justify-content: center;
  }
  .site-url {
    width: 379px; height: 30px; margin-left: 3px;
    border: 1.5px solid var(--text-white);
    color: var(--text-white); font-weight: 500; font-size: 18px; letter-spacing: 2.5px;
    display: flex; align-items: center; justify-content: center;
  }
</style>
</head>
<body>
<div class="canvas">
  <section class="banner">
    <div class="band-top"></div>
    <div class="band-mid"></div>
    <div class="band-bottom"></div>

    <svg class="feature-art" viewBox="0 0 1045 435" role="img"
         aria-label="Soft green leafy photo backdrop with the book shown as a paperback, a tablet and a phone">
      <defs>
        <linearGradient id="leafGlow" x1="0" y1="0" x2="1" y2="1">
          <stop offset="0" stop-color="var(--leaf-light)"/>
          <stop offset="0.55" stop-color="var(--green)"/>
          <stop offset="1" stop-color="var(--leaf-deep)"/>
        </linearGradient>
      </defs>
      <path d="M 770 0 Q 640 120 652 435" fill="none" stroke="var(--accent-red)" stroke-width="5"/>
      <path d="M 792 0 Q 662 130 672 435 L 1045 435 L 1045 0 Z" fill="url(#leafGlow)"/>
    </svg>

    <div class="headline-lead">CLEARING A COURT</div>
    <div class="headline-main">DEBT MARK</div>

    <div class="author-pill">A BOOK BY <span class="author-name">DANIEL HARTLEY</span></div>

    <p class="tagline">A simple jargon-free guide to removing a County Court Judgment from your credit record, improving your credit score and finding financial freedom.</p>

    <div class="availability">
      <span class="highlight">Available now</span> on
      <span class="store-name">Shelfway</span>
      in paperback and as an e-book.
    </div>

    <div class="cta-row">
      <div class="cta-button">Book Now</div>
      <div class="site-url">www.thornridgelaw.co.uk</div>
    </div>
  </section>
</div>
</body>
</html>
```